ALL TEXT GRAPHICS RK May 2025 for Instagram

We are looking for a series of social media graphics for Instagram (new size: 4:5 (1080 x 1350 pixels) ratio that are ALL TEXT. We want the following quotes below on each graphic; one quote per graphic. AND, In very small letters at the bottom of each graphic, add @RKBexleyOnline
The look and feel of these graphics should be complimentary to the color palette attached below; but keep them simple. But the design is up to you; at the end of this document, I provided various samples of all text graphics that I like as examples.
women looking to lose weight

```html
<!DOCTYPE html>
<html lang="en">
<head>
<meta charset="utf-8">
<title>RK Instagram Text Graphics</title>
<link href="https://fonts.googleapis.com/css2?family=Asap+Condensed:wght@400;500;800;900&family=Playball&display=swap" rel="stylesheet">
<style>
  :root {
    --bg-pink: #ff66ad;
    --card-white: #ffffff;
    --deep-magenta: #d4006b;
    --soft-pink: #f26aac;
  }
  * { margin: 0; padding: 0; box-sizing: border-box; }
  html, body { width: 732px; height: 1200px; overflow: hidden; }
  body {
    background: var(--bg-pink);
    font-family: "Asap Condensed", "Arial Narrow", sans-serif;
    color: var(--deep-magenta);
    position: relative;
  }
  .post {
    position: absolute;
    width: 228px;
    height: 285px;
    background: var(--card-white);
    border-radius: 14px;
    display: flex;
    flex-direction: column;
    align-items: center;
    justify-content: center;
    text-align: center;
    padding: 10px 8px 34px;
  }
  .col-1 { left: 19.5px; } .col-2 { left: 252px; } .col-3 { left: 484.5px; }
  .row-1 { top: 23px; } .row-2 { top: 313px; } .row-3 { top: 602px; } .row-4 { top: 892px; }
  .headline {
    font-weight: 900;
    font-size: 27px;
    line-height: 0.95;
    text-transform: uppercase;
    letter-spacing: 0.2px;
  }
  .headline.mixed { text-transform: none; }
  .body {
    font-weight: 400;
    font-size: 15px;
    line-height: 1.2;
    margin-top: 10px;
  }
  .body.caps { text-transform: uppercase; }
  .body.roomy { line-height: 1.55; }
  .script {
    font-family: "Playball", cursive;
    color: var(--soft-pink);
    font-size: 33px;
    line-height: 0.85;
    margin-top: 12px;
  }
  .inline-script {
    font-family: "Playball", cursive;
    color: var(--soft-pink);
    font-size: 22px;
    text-transform: none;
  }
  .handle {
    position: absolute;
    bottom: 13px;
    left: 0; right: 0;
    font-size: 10px;
    font-weight: 500;
    text-align: center;
  }
</style>
</head>
<body>

<section class="post col-1 row-1">
  <h2 class="headline" style="font-size:29px">Tired.<br>Moody.<br>Stubborn<br>Belly Fat.</h2>
  <p class="body caps">Your hormones are<br>screaming for help!</p>
  <p class="script">Let’s fix that.</p>
  <p class="handle">@RKBexleyOnline</p>
</section>

<section class="post col-2 row-1">
  <h2 class="headline mixed" style="font-size:30px">That stubborn<br>weight?</h2>
  <p class="body" style="margin-top:16px">It’s not your fault.<br>Your hormones are to<br>blame and you’re not alone;</p>
  <p class="script" style="margin-top:22px">But there is<br>a fix.</p>
  <p class="handle">@RKBexleyOnline</p>
</section>

<section class="post col-3 row-1">
  <h2 class="headline">Your belly<br>isn’t fat...<br>it’s hormonal.</h2>
  <p class="body caps roomy" style="margin-top:22px">And here’s how to fix it.<br>Comment <span class="inline-script">Hormones</span><br>if nothing is working.</p>
  <p class="handle">@RKBexleyOnline</p>
</section>

<section class="post col-1 row-2">
  <h2 class="headline">The stubborn<br>belly fat<br>after 40?</h2>
  <p class="body roomy" style="margin-top:14px">It’s not about calories;<br>it’s about your hormones.</p>
  <p class="script" style="margin-top:10px">Here is the fix!</p>
  <p class="handle">@RKBexleyOnline</p>
</section>

<section class="post col-2 row-2">
  <h2 class="headline">Flat tummy<br>in<br>your 40s?</h2>
  <p class="body caps roomy" style="margin-top:12px">It’s still possible!<br>Comment <span class="inline-script">Bye Belly</span><br>to get the 10 secrets<br>to a flatter tummy</p>
  <p class="handle">@RKBexleyOnline</p>
</section>

<section class="post col-3 row-2">
  <h2 class="headline">Bloating.<br>Muffin top.<br>Puffy waistline.</h2>
  <p class="body roomy" style="margin-top:14px">Your body’s screaming<br>for a different kind of fix.</p>
  <p class="script" style="margin-top:10px">Here it is</p>
  <p class="handle">@RKBexleyOnline</p>
</section>

<section class="post col-1 row-3">
  <h2 class="headline">You’re doing<br>all<br>the “right”<br>things,</h2>
  <p class="body caps roomy" style="margin-top:8px">You’re doing all<br>the “right” things, but<br>your belly won’t go down?<br>Here’s what you<br>haven’t tried.</p>
  <p class="handle">@RKBexleyOnline</p>
</section>

<section class="post col-2 row-3">
  <h2 class="headline">This 90-day plan<br>helped women<br>over 40<br>slim down,</h2>
  <p class="body caps roomy" style="margin-top:12px">Get a tiny waist<br>and feel sexy again.</p>
  <p class="script" style="margin-top:12px">You’re next.</p>
  <p class="handle">@RKBexleyOnline</p>
</section>

<section class="post col-3 row-3">
  <h2 class="headline">This is the<br>secret women<br>over 40<br>are using<br>to get snatched;<br>without<br>starving.</h2>
  <p class="body caps roomy" style="margin-top:10px">Comment <span class="inline-script">Skinny</span> to<br>get the exact plan.</p>
  <p class="handle">@RKBexleyOnline</p>
</section>

<section class="post col-2 row-4">
  <h2 class="headline mixed">What worked in<br>your 30s won’t<br>work now.</h2>
  <p class="body" style="font-size:18px;line-height:1.55;margin-top:14px">Here’s what<br>actually does.<br>Drop 30 Pounds<br>in 3 Months.</p>
  <p class="handle">@RKBexleyOnline</p>
</section>

</body>
</html>
```